DEAN COLLOPY PROPERTY SERVICES

I want a business card that is clean and simple.
'Dean Collopy Property Services' is the title.
Somewhere on the card needs to be 'Carpentry, Tiling, painting and garden services'

On the back of card
PH 087 394 1526
email: deancollopypropertyservices@bluefinchmail.net

I have attached a picture of my other business. I would like the font and design to be similar to the bathroom business.

Many thanks.

```html
<!DOCTYPE html>
<html lang="en">
<head>
<meta charset="utf-8">
<title>Dean Collopy Property Services – Business Card</title>
<link rel="stylesheet" href="https://fonts.googleapis.com/css2?family=Montserrat:wght@300;400;500;600&display=swap">
<style>
  :root {
    --backdrop: #929292;
    --card: #f7f7f7;
    --ink: #0a0a0a;
    --ink-soft: #1c1c1c;
    --band-text: #ffffff;
  }
  * { margin: 0; padding: 0; box-sizing: border-box; }
  html, body {
    width: 1200px;
    height: 800px;
    overflow: hidden;
    background: var(--backdrop);
    font-family: "Montserrat", Arial, sans-serif;
  }
  .canvas {
    position: relative;
    width: 1200px;
    height: 800px;
    display: flex;
    align-items: center;
    justify-content: center;
    gap: 40px;
  }
  .card {
    position: relative;
    width: 540px;
    height: 327px;
    background: var(--card);
    box-shadow: 0 14px 30px rgba(0, 0, 0, 0.22);
    overflow: hidden;
  }

  /* Front */
  .card-front .title {
    position: absolute;
    left: 70px;
    top: 92px;
    color: var(--ink);
  }
  .card-front .title-name {
    display: block;
    font-weight: 500;
    font-size: 50px;
    line-height: 1;
    letter-spacing: 0.5px;
  }
  .card-front .title-trade {
    display: block;
    margin-top: 6px;
    margin-left: 6px;
    font-weight: 300;
    font-size: 24px;
    letter-spacing: 3px;
    color: var(--ink-soft);
  }
  .card-front .services-band {
    position: absolute;
    left: 0;
    right: 0;
    bottom: 0;
    height: 46px;
    background: var(--ink);
    display: flex;
    align-items: center;
    justify-content: center;
  }
  .card-front .services {
    color: var(--band-text);
    font-weight: 500;
    font-size: 13px;
    letter-spacing: 3.2px;
  }

  /* Back */
  .card-back .contact-band {
    position: absolute;
    left: 0;
    right: 0;
    top: 100px;
    height: 112px;
    background: var(--ink);
    display: flex;
    flex-direction: column;
    align-items: center;
    justify-content: center;
    gap: 14px;
  }
  .card-back .contact-line {
    display: flex;
    align-items: center;
    gap: 10px;
    color: var(--band-text);
    font-weight: 500;
    font-size: 15px;
    letter-spacing: 0.6px;
  }
  .card-back .contact-icon {
    width: 20px;
    height: 20px;
    flex: none;
  }
</style>
</head>
<body>
<main class="canvas">

  <section class="card card-front" aria-label="Business card front">
    <h1 class="title">
      <span class="title-name">Dean Collopy</span>
      <span class="title-trade">Property Services</span>
    </h1>
    <div class="services-band">
      <p class="services">Carpentry, Tiling, Painting and Garden Services</p>
    </div>
  </section>

  <section class="card card-back" aria-label="Business card back">
    <div class="contact-band">
      <p class="contact-line">
        <svg class="contact-icon" viewBox="0 0 24 24" aria-hidden="true">
          <path fill="#fff" d="M6.6 10.8a15.1 15.1 0 0 0 6.6 6.6l2.2-2.2a1 1 0 0 1 1-.25 11.4 11.4 0 0 0 3.6.57 1 1 0 0 1 1 1V20a1 1 0 0 1-1 1A17 17 0 0 1 3 4a1 1 0 0 1 1-1h3.5a1 1 0 0 1 1 1c0 1.25.2 2.45.57 3.57a1 1 0 0 1-.25 1z"/>
          <path fill="none" stroke="#fff" stroke-width="1.8" stroke-linecap="round" d="M14.5 3.5a6.5 6.5 0 0 1 6 6M14.5 7a3 3 0 0 1 2.5 2.5"/>
        </svg>
        <span>087 394 1526</span>
      </p>
      <p class="contact-line">
        <svg class="contact-icon" viewBox="0 0 24 24" aria-hidden="true">
          <rect x="2" y="5" width="20" height="14" rx="1" fill="#fff"/>
          <path d="M3 6.5l9 6.5 9-6.5" fill="none" stroke="#0a0a0a" stroke-width="1.6"/>
        </svg>
        <span>deancollopypropertyservices@bluefinchmail.net</span>
      </p>
    </div>
  </section>

</main>
</body>
</html>
```